Lantern Hour book needs a cover design

I need a front and back cover design that demonstrates a strong sense of possibility that trust can be repaired even if things look bleak. Repairing trust is difficult, but this book is full of wisdom, proven strategies, and doctoral research to help people strengthen relationships and improve trust. It can help any group: business, nonprofit, education, service. Showing diversity of groups and people is very important. For the cover title, there should be a play on words: "Lantern Hour: Is it? Possible" should have the words "is it?" crossed out and the words "It IS! should be replaced there in a striking way. Perhaps in red ink. For publishing purposes, book will be titled Lantern Hour: It IS Possible! Please see the attachment for an example. The book layout is approximately 260 pages.

Target Market(s)

A business self-help book, but the target is any person in a group that feels they have lost trust in each other. It can be just a normal person struggling in a volunteer group they are a part of, or a supervisor whose group is not working well together. It can be a leader who just wants their group to be stronger.

Industry/Entity Type

Business Management

Font styles to use
Other font styles liked:
• Allise - I believe is being used on the interior of the book for the title page and headings

Requirements
Must have
• Show hope and possibility in the midst of difficulty. Must have a play on the words in the title "Lantern Hour: Is it? Possible" with crossing out "is it?" with "It IS!" (see attached example) Must include the author's name: Marla Quinby, PhD Must include a smaller tagline: "Tested Ways to Help Teams Move Forward"
Nice to have
• Showing diverse people, or hands. Diverse kinds of groups - not just business. A colorful cover. Maybe show the complexity of trust when it is broken...broken pieces of trust that are then picked up and put together when people work together. Could show people (or images of hands) or other ways to show that it's a choice and it is possible to repair broken trust. I'd also like to convey a sense of a group - not just random people. That they have something at stake to work on repairing trust together and this book can help them.
Should not have
• If images of people are used, just showing one gender or race is not okay. Nor just binary choices: like an image containing one man and one woman, or one white person and one person of color - otherwise it seems that the book on Lantern Hour is about race or gender relations.

```html
<!DOCTYPE html>
<html lang="en">
<head>
<meta charset="utf-8">
<title>Lantern Hour — Front Cover</title>
<link rel="stylesheet" href="https://fonts.googleapis.com/css2?family=Federo&family=Delius&family=Pontano+Sans:wght@400;600&display=swap">
<style>
  :root {
    --page-bg: #e4e7ea;
    --cover-bg: #ffffff;
    --title-blue: #1d7fb4;
    --title-purple: #5b2d8e;
    --accent-orange: #e8562a;
    --text-grey: #6b6b6b;
    --art-blue: #2d8bc4;
    --art-purple: #5a3c9a;
  }
  html, body {
    margin: 0;
    width: 1200px;
    height: 1200px;
    overflow: hidden;
    background: var(--page-bg);
  }
  .canvas {
    width: 1200px;
    height: 1200px;
    display: flex;
    align-items: center;
    justify-content: center;
  }
  .book-cover {
    width: 680px;
    height: 1080px;
    background: var(--cover-bg);
    box-shadow: 0 6px 24px rgba(0,0,0,0.12);
  }
  .book-cover svg { display: block; }
  .title-word { font-family: "Federo", sans-serif; }
  .label-word { font-family: "Pontano Sans", sans-serif; }
  .body-text { font-family: "Delius", cursive; }
</style>
</head>
<body>
<main class="canvas">
  <article class="book-cover">
    <svg width="680" height="1080" viewBox="0 0 680 1080" xmlns="http://www.w3.org/2000/svg">
      <defs>
        <radialGradient id="heroArtTone" cx="50%" cy="50%" r="60%">
          <stop offset="0%" stop-color="#7a9fd8"/>
          <stop offset="60%" stop-color="var(--art-blue)"/>
          <stop offset="100%" stop-color="var(--art-purple)"/>
        </radialGradient>
        <radialGradient id="horizonGlow" cx="50%" cy="50%" r="50%">
          <stop offset="0%" stop-color="#ffffff" stop-opacity="0.95"/>
          <stop offset="100%" stop-color="#ffffff" stop-opacity="0"/>
        </radialGradient>
      </defs>

      <g class="publisher-imprint">
        <rect x="520" y="76" width="16" height="16" fill="var(--text-grey)"/>
        <text class="label-word" x="542" y="83" font-size="12" fill="var(--text-grey)">NORTHGATE</text>
        <text class="label-word" x="542" y="96" font-size="12" fill="var(--text-grey)">PRESS</text>
      </g>

      <rect class="hero-art" x="275" y="50" width="150" height="150" rx="75"
            fill="url(#heroArtTone)" opacity="0.9"
            role="img" aria-label="Illustration of people climbing interlocking gears toward a flag"/>

      <text class="title-word" x="340" y="440" text-anchor="middle"
            font-size="230" fill="var(--title-blue)"
            textLength="560" lengthAdjust="spacingAndGlyphs">LANTERN</text>
      <text class="title-word" x="350" y="665" text-anchor="middle"
            font-size="240" fill="var(--title-purple)"
            textLength="470" lengthAdjust="spacingAndGlyphs">HOUR</text>

      <path class="horizon-arc" d="M 90 705 Q 340 625 600 690 Q 340 648 90 705 Z" fill="var(--title-purple)"/>
      <ellipse cx="370" cy="660" rx="70" ry="34" fill="url(#horizonGlow)"/>

      <g class="struck-question">
        <text class="body-text" x="330" y="748" text-anchor="middle" font-size="40" fill="var(--text-grey)">Is it?</text>
        <path d="M 282 744 L 378 724" stroke="var(--accent-orange)" stroke-width="4" fill="none" stroke-linecap="round"/>
        <path d="M 286 722 L 372 748" stroke="var(--accent-orange)" stroke-width="4" fill="none" stroke-linecap="round"/>
        <path d="M 372 724 L 420 708" stroke="var(--accent-orange)" stroke-width="3" fill="none" stroke-linecap="round"/>
      </g>

      <g class="answer-line">
        <rect x="150" y="762" width="40" height="80" fill="var(--title-purple)"/>
        <text class="label-word" x="170" y="802" font-size="26" fill="#ffffff"
              text-anchor="middle" dominant-baseline="middle"
              transform="rotate(-90 170 802)">It Is</text>
        <text class="label-word" x="196" y="842" font-size="104" fill="var(--title-blue)"
              textLength="340" lengthAdjust="spacingAndGlyphs">Possible</text>
      </g>

      <text class="body-text" x="350" y="900" text-anchor="middle" font-size="25" fill="var(--text-grey)">Tested Ways to Help</text>
      <text class="body-text" x="350" y="934" text-anchor="middle" font-size="25" fill="var(--text-grey)">Teams Move Forward</text>

      <text class="body-text" x="345" y="1010" text-anchor="middle" font-size="32" fill="var(--title-blue)">Marla Quinby, PhD</text>
    </svg>
  </article>
</main>
</body>
</html>
```